Parkinson's Disease Progression

Visually describe the rate of Parkinson progression in the first 15 years following diagnosis. Title: "Patient-Perceived Progression of Parkinsonism"

The attached figure names "meanqol" is the curve that should serve as the basis of this graphic. Everything else-- color, labels, font, etc. describe this curve.
Thank you!

Target Market(s)

People with Parkisnon's Disease, neurologists, family members.

Font styles to use
Sans Serif

Requirements
Must have
• Must have the lines going through these exact numbers
Excellent -- 502
Very good- 661
Good- 895
Fair- 1268
Poor- 1655

LABELS:
Title: "Patient-Perceived Progression of Parkinsonism"
"SAW-MX (Self-Assessed Wellbeing Index for Movement Conditions)" should be the label on the left.
"Quality of Life" should be the label on the right
"Years Since Diagnosis" should be the label on the bottom
Nice to have
• A color scheme that goes from GOOD (low numbers) to BAD (high numbers).

Easy to read (elderly)

```html
<!DOCTYPE html>
<html lang="en">
<head>
<meta charset="utf-8">
<title>Patient-Perceived Progression of Parkinsonism</title>
<link rel="stylesheet" href="https://fonts.googleapis.com/css2?family=Poppins:wght@400;500&display=swap">
<style>
  :root{
    --bg:#ffffff;
    --ink:#1d1d1f;
    --axis-bar:#7d8791;
    --axis-text:#ffffff;
    --line-grey:#7a8591;
    --band-dark:#5a4a2c;
  }
  html,body{margin:0;padding:0;width:1200px;height:614px;overflow:hidden;background:var(--bg);}
  .board{display:block;width:1200px;height:614px;font-family:"Poppins",Arial,sans-serif;}
  .chart-title{font-size:15px;font-weight:500;fill:var(--ink);}
  .tick{font-size:12px;fill:var(--ink);}
  .axis-title{font-size:12.5px;font-weight:500;fill:var(--ink);}
  .bar-label{font-size:11.5px;font-weight:500;fill:var(--axis-text);}
  .quality-label{font-size:12px;fill:#3a2a20;}
  .axis-bar{fill:var(--axis-bar);}
</style>
</head>
<body>
<svg class="board" viewBox="0 0 1164 596" preserveAspectRatio="none" role="img" aria-label="Two versions of a chart of patient-perceived progression of Parkinsonism over 15 years">
  <defs>
    <linearGradient id="poor" x1="0" y1="0" x2="0" y2="1"><stop offset="0" stop-color="#d94848"/><stop offset="1" stop-color="#ee7b78"/></linearGradient>
    <linearGradient id="fair" x1="0" y1="0" x2="0" y2="1"><stop offset="0" stop-color="#e97a3d"/><stop offset="1" stop-color="#f6a877"/></linearGradient>
    <linearGradient id="good" x1="0" y1="0" x2="0" y2="1"><stop offset="0" stop-color="#efb23a"/><stop offset="1" stop-color="#f7d06f"/></linearGradient>
    <linearGradient id="verygood" x1="0" y1="0" x2="0" y2="1"><stop offset="0" stop-color="#78b142"/><stop offset="1" stop-color="#a5d26a"/></linearGradient>
    <linearGradient id="excellent-teal" x1="0" y1="0" x2="0" y2="1"><stop offset="0" stop-color="#3cc1aa"/><stop offset="1" stop-color="#76e1cd"/></linearGradient>
    <linearGradient id="excellent-blue" x1="0" y1="0" x2="0" y2="1"><stop offset="0" stop-color="#86c6f8"/><stop offset="1" stop-color="#4a9cef"/></linearGradient>
  </defs>

  <!-- Version A -->
  <g class="chart chart--light">
    <text class="chart-title" x="286" y="131" text-anchor="middle">Patient-Perceived Progression of Parkinsonism</text>
    <rect class="axis-bar" x="25" y="155" width="30" height="282"/>
    <text class="bar-label" transform="translate(45 296) rotate(-90)" text-anchor="middle">SAW-MX</text>
    <g class="bands">
      <rect x="97" y="155" width="318" height="68" fill="url(#poor)"/>
      <rect x="97" y="223" width="318" height="66" fill="url(#fair)"/>
      <rect x="97" y="289" width="318" height="41" fill="url(#good)"/>
      <rect x="97" y="330" width="318" height="28" fill="url(#verygood)"/>
      <rect x="97" y="358" width="318" height="79" fill="url(#excellent-teal)"/>
      <g stroke="#ffffff" stroke-opacity=".6" stroke-width="1"><line x1="97" y1="223" x2="415" y2="223"/><line x1="97" y1="289" x2="415" y2="289"/><line x1="97" y1="330" x2="415" y2="330"/><line x1="97" y1="358" x2="415" y2="358"/></g>
    </g>
    <g class="ticks-y">
      <text class="tick" x="88" y="165" text-anchor="end">1655</text>
      <text class="tick" x="88" y="233" text-anchor="end">1268</text>
      <text class="tick" x="88" y="298" text-anchor="end">895</text>
      <text class="tick" x="88" y="340" text-anchor="end">661</text>
      <text class="tick" x="88" y="367" text-anchor="end">512</text>
    </g>
    <path d="M97,345 C140,326 170,308 204,305 C250,300 270,293 309,272 C350,252 385,236 415,224 L415,286 C385,290 350,296 309,307 C265,322 250,331 204,336 C170,340 140,372 97,405 Z" fill="#ffffff" fill-opacity=".45"/>
    <path d="M97,352 C140,333 170,314 204,311 C250,306 270,299 309,279 C350,260 385,246 415,236 L415,276 C385,280 350,287 309,299 C265,315 250,325 204,329 C170,333 140,362 97,392 Z" fill="#ffffff"/>
    <path d="M97,369 C140,345 170,322 204,319 C250,315 265,312 309,290 C350,270 380,260 415,255" fill="none" stroke="var(--line-grey)" stroke-width="2"/>
    <circle cx="97" cy="369" r="4.5" fill="#3cc1aa"/>
    <circle cx="204" cy="319" r="4.5" fill="#efb23a"/>
    <circle cx="309" cy="290" r="4.5" fill="#efb23a"/>
    <circle cx="415" cy="255" r="4.5" fill="#e97a3d"/>
    <g class="ticks-x">
      <text class="tick" x="97" y="463" text-anchor="middle">0</text>
      <text class="tick" x="204" y="463" text-anchor="middle">5</text>
      <text class="tick" x="309" y="463" text-anchor="middle">10</text>
      <text class="tick" x="415" y="463" text-anchor="middle">15</text>
    </g>
    <text class="axis-title" x="263" y="492" text-anchor="middle">Years Since Diagnosis</text>
    <g class="quality-scale">
      <rect x="424" y="155" width="97" height="68" fill="url(#poor)"/>
      <rect x="424" y="223" width="97" height="66" fill="url(#fair)"/>
      <rect x="424" y="289" width="97" height="41" fill="url(#good)"/>
      <rect x="424" y="330" width="97" height="28" fill="url(#verygood)"/>
      <rect x="424" y="358" width="97" height="79" fill="url(#excellent-teal)"/>
      <g stroke="#ffffff" stroke-opacity=".6"><line x1="424" y1="223" x2="521" y2="223"/><line x1="424" y1="289" x2="521" y2="289"/><line x1="424" y1="330" x2="521" y2="330"/><line x1="424" y1="358" x2="521" y2="358"/></g>
      <text class="quality-label" x="472" y="195" text-anchor="middle">Poor</text>
      <text class="quality-label" x="472" y="261" text-anchor="middle">Fair</text>
      <text class="quality-label" x="472" y="315" text-anchor="middle">Good</text>
      <text class="quality-label" x="472" y="349" text-anchor="middle">Very good</text>
      <text class="quality-label" x="472" y="403" text-anchor="middle">Excellent</text>
    </g>
    <rect class="axis-bar" x="527" y="155" width="30" height="282"/>
    <text class="bar-label" transform="translate(546 296) rotate(-90)" text-anchor="middle">Quality of Life</text>
  </g>

  <!-- Version B -->
  <g class="chart chart--deep">
    <text class="chart-title" x="868" y="131" text-anchor="middle">Patient-Perceived Progression of Parkinsonism</text>
    <rect class="axis-bar" x="605" y="155" width="31" height="282"/>
    <text class="bar-label" transform="translate(626 296) rotate(-90)" text-anchor="middle">SAW-MX</text>
    <g class="ticks-y">
      <text class="tick" transform="translate(661 158) rotate(-90)" text-anchor="end">1655</text>
      <text class="tick" transform="translate(661 226) rotate(-90)" text-anchor="end">1268</text>
      <text class="tick" transform="translate(661 289) rotate(-90)" text-anchor="end">895</text>
      <text class="tick" transform="translate(661 331) rotate(-90)" text-anchor="end">661</text>
      <text class="tick" transform="translate(661 357) rotate(-90)" text-anchor="end">512</text>
    </g>
    <g class="bands">
      <rect x="678" y="155" width="319" height="68" fill="url(#poor)"/>
      <rect x="678" y="223" width="319" height="66" fill="url(#fair)"/>
      <rect x="678" y="289" width="319" height="41" fill="url(#good)"/>
      <rect x="678" y="330" width="319" height="28" fill="url(#verygood)"/>
      <rect x="678" y="358" width="319" height="79" fill="url(#excellent-blue)"/>
    </g>
    <path d="M678,345 C720,325 750,306 784,303 C830,298 850,292 890,270 C930,250 965,236 997,220 L997,286 C965,290 930,297 890,309 C850,324 830,332 784,337 C750,342 720,368 678,398 Z" fill="var(--band-dark)" fill-opacity=".6"/>
    <path d="M678,370 C720,346 750,323 784,320 C830,316 845,313 890,292 C930,272 960,260 996,255" fill="none" stroke="#ffffff" stroke-width="2"/>
    <g fill-opacity=".9" stroke="#ffffff" stroke-width="2">
      <circle cx="678" cy="370" r="7" fill="#4a9cef"/>
      <circle cx="784" cy="320" r="7" fill="#efb23a"/>
      <circle cx="890" cy="292" r="7" fill="#efb23a"/>
      <circle cx="996" cy="255" r="7" fill="#e97a3d"/>
    </g>
    <g fill="none" stroke="#ffffff" stroke-width="1.5">
      <circle cx="678" cy="370" r="3.5"/><circle cx="784" cy="320" r="3.5"/><circle cx="890" cy="292" r="3.5"/><circle cx="996" cy="255" r="3.5"/>
    </g>
    <g class="ticks-x">
      <text class="tick" x="678" y="463" text-anchor="middle">0</text>
      <text class="tick" x="784" y="463" text-anchor="middle">5</text>
      <text class="tick" x="890" y="463" text-anchor="middle">10</text>
      <text class="tick" x="996" y="463" text-anchor="middle">15</text>
    </g>
    <text class="axis-title" x="846" y="492" text-anchor="middle">Years Since Diagnosis</text>
    <rect class="axis-bar" x="1003" y="155" width="31" height="282"/>
    <text class="bar-label" transform="translate(1023 296) rotate(-90)" text-anchor="middle">Quality of Life</text>
    <g class="quality-scale">
      <rect x="1040" y="155" width="97" height="68" fill="url(#poor)"/>
      <rect x="1040" y="223" width="97" height="66" fill="url(#fair)"/>
      <rect x="1040" y="289" width="97" height="41" fill="url(#good)"/>
      <rect x="1040" y="330" width="97" height="28" fill="url(#verygood)"/>
      <rect x="1040" y="358" width="97" height="79" fill="url(#excellent-blue)"/>
      <text class="quality-label" x="1088" y="195" text-anchor="middle">Poor</text>
      <text class="quality-label" x="1088" y="261" text-anchor="middle">Fair</text>
      <text class="quality-label" x="1088" y="315" text-anchor="middle">Good</text>
      <text class="quality-label" x="1088" y="349" text-anchor="middle">Very good</text>
      <text class="quality-label" x="1088" y="403" text-anchor="middle">Excellent</text>
    </g>
  </g>
</svg>
</body>
</html>
```